BRTW Traditional Business Card Project

Please see attached....just a simple business card... on attachment- please use the exact font, style, etc as the attached "Dal Rupert Huxley" card... however, replace with the "Owen Bartholomew Lindqvist" text and address below the card.

```html
<!DOCTYPE html>
<html lang="en">
<head>
<meta charset="utf-8">
<title>BRTW Business Card</title>
<link rel="stylesheet" href="https://fonts.googleapis.com/css2?family=Tinos:wght@400&display=swap">
<style>
  :root {
    --backdrop: #262626;
    --card-frame: #7b7c7c;
    --card-face: #d0d5d3;
    --ink: #111111;
  }
  * { margin: 0; padding: 0; box-sizing: border-box; }
  html, body {
    width: 1200px;
    height: 895px;
    overflow: hidden;
    background: var(--backdrop);
  }
  .business-card {
    position: absolute;
    left: 110px;
    top: 167px;
    width: 980px;
    height: 560px;
    background: var(--card-frame);
    padding: 18px;
  }
  .card-face {
    position: relative;
    width: 100%;
    height: 100%;
    background: var(--card-face);
    color: var(--ink);
    font-family: "Tinos", "Times New Roman", serif;
  }
  .firm-name {
    position: absolute;
    left: 40px;
    top: 30px;
    font-variant: small-caps;
    line-height: 1.05;
  }
  .firm-name .firm-primary { display: block; font-size: 27px; }
  .firm-name .firm-secondary { display: block; font-size: 19px; padding-left: 46px; }
  .attorney {
    position: absolute;
    left: 50px;
    width: 600px;
    top: 196px;
    text-align: center;
    white-space: nowrap;
  }
  .attorney-name {
    font-size: 44px;
    font-variant: small-caps;
    letter-spacing: 0.3px;
    font-weight: 400;
    line-height: 1.1;
  }
  .attorney-title {
    font-size: 19px;
    letter-spacing: 0.5px;
    margin-top: 4px;
    padding-left: 180px;
  }
  .contact-lines {
    position: absolute;
    right: 34px;
    top: 214px;
    text-align: right;
    font-size: 24px;
    line-height: 1.15;
    white-space: nowrap;
  }
  .office-address {
    position: absolute;
    left: 40px;
    bottom: 30px;
    font-size: 24px;
    line-height: 1.15;
    white-space: nowrap;
  }
</style>
</head>
<body>
  <div class="business-card">
    <div class="card-face">
      <div class="firm-name">
        <span class="firm-primary">Bright River</span>
        <span class="firm-secondary">Trial Works, PLC</span>
      </div>
      <div class="attorney">
        <h1 class="attorney-name">Owen Bartholomew Lindqvist</h1>
        <p class="attorney-title">ATTORNEY AT LAW</p>
      </div>
      <div class="contact-lines">
        <p>TEL (555) 214-3300</p>
        <p>FAX (555) 214-3301</p>
        <p>olindqvist@lawbrtw.com</p>
      </div>
      <div class="office-address">
        <p>2417 CEDAR LANE, SUITE B</p>
        <p>MAPLE GROVE, CA 90412</p>
        <p>www.lawbrtw.com</p>
      </div>
    </div>
  </div>
</body>
</html>
```